Smart Repair Business, 2 sided tri fold leaflet/flyer

Hi I'm after a tri fold flyer for a smart repair business, there are two employees, myself and Derek. I have attached a scan of a flyer from another local smart repair business that pretty much ticks all the boxes for what I would like however I don't want to copy him 100% but the design and layout are perfect so don't want to steer too far away from them. It's a double side document. The files are called "Tri fold flyer design Outside.pdf" & "Tri fold flyer design Inside.pdf"

The size i possibly require as stated by printhollow is as follows;
Full Bleed Size (starting document size)
282 x 219 mm
3331 x 2588 pixels
* Finished artwork should use the full bleed dimensions for best results.
Document Trim Size (final size after being cut)
279 x 216 mm
3295 x 2551 pixels
ive attached 2 templates (front and back) which printhollow supply

Although if you see the uploaded flyer i like the look of the front page is staggered back slightly, I've found that the printhollow Brochures come pre folded but if I get it printed as a double sided flyer I can fold them myself with the staggered front page,

I do not have an image of a car to use as used in the leaflet I've attached, I was hoping that is something that can be supplied but if not I can try source something.

Feel free to use any of the content from my website or facebook page
My website address is www.quillardpanelworks.com
my facebook address is www.facebook.com/quillardpanelworks

Ive attached the file of our business cards for reference of any information.
Also attached is a large copy of our company logo which I would like included

I am also happy to take any pictures of anything requested or send any originals I can find.

Requirements
Must have
• Must have the following contact information;

Keith 07700900418
Derek 07700900273
Office (answerphone) 01632 960581
email: allstaff@quillardpanelworks.com
website: www.quillardpanelworks.com
Nice to have
• If I can somehow have a picture including my paint van would be great if it can be fitted anywhere as it stands out around town so people may link it with seeing the flyer.

I would like to have the QR code which I have attached the file for.

Also somewhere mentioning that via my website a contact form can be filled out and a photo of the damage uploaded and sent.
Should not have
• should not have anything on paintless dent removal (PDR) as this is not a service we offer

```html
<!DOCTYPE html>
<html lang="en">
<head>
<meta charset="utf-8">
<title>The Panelsmith – Tri-fold Leaflet, Outside</title>
<link href="https://fonts.googleapis.com/css2?family=Oswald:wght@400;600&family=Open+Sans:wght@400;600&display=swap" rel="stylesheet">
<style>
  :root{
    --bg:#e4e6ea;
    --navy:#14174d;
    --navy-2:#1d2268;
    --sky:#2bb3e8;
    --sky-light:#6fd0f3;
    --royal:#2f5fc4;
    --white:#ffffff;
    --paper:#f4f5f7;
    --ink:#2a2d3a;
    --muted:#b9c6ec;
  }
  *{margin:0;padding:0;box-sizing:border-box}
  html,body{width:1200px;height:1024px;overflow:hidden;background:var(--bg)}
  body{font-family:"Open Sans",Arial,sans-serif;color:var(--ink)}
  .leaflet{position:absolute;left:40px;top:78px;width:1120px;height:867px;display:flex;box-shadow:0 6px 24px rgba(0,0,0,.18)}
  .panel{position:relative;width:373.33px;height:100%;overflow:hidden}
  .panel svg.deco{position:absolute;inset:0;width:100%;height:100%}
  .caps{font-family:"Oswald",Arial,sans-serif;text-transform:uppercase}

  /* left panel */
  .panel--about{background:var(--white)}
  .about__title{position:absolute;top:34px;left:30px;right:80px;text-align:center;font-family:"Oswald",Arial,sans-serif;font-weight:600;font-size:28px;color:var(--sky);letter-spacing:.5px}
  .about__text{position:absolute;top:84px;left:30px;right:30px;font-size:12.5px;line-height:1.55;color:var(--ink)}
  .about__photo{position:absolute;top:440px;left:0;right:0;height:240px;background:linear-gradient(160deg,#c9b8a4 0%,#8f6a55 40%,#4d5d85 75%,#2a2f45 100%)}
  .about__cta{position:absolute;left:26px;right:26px;top:712px;text-align:center}
  .about__cta-head{font-weight:600;font-size:20px;color:var(--sky);line-height:1.2}
  .phones{font-family:"Oswald",Arial,sans-serif;font-weight:600;color:var(--navy);display:flex;justify-content:center;gap:10px;align-items:center}
  .phones svg{width:12px;height:16px;fill:var(--sky)}
  .about__cta .phones{font-size:20px;margin-top:8px}
  .web{font-family:"Oswald",Arial,sans-serif;font-weight:600;color:var(--navy);text-transform:uppercase}
  .about__cta .web{font-size:15px;margin-top:4px}

  /* middle panel */
  .panel--faq{background:var(--navy)}
  .faq{position:absolute;top:66px;left:28px;right:28px;color:var(--white)}
  .faq__title{font-size:19px;color:var(--sky-light);margin-bottom:12px}
  .faq__item{margin-bottom:11px;font-size:12.5px;line-height:1.42}
  .faq__q{color:var(--white)}
  .faq__a{color:var(--muted)}
  .contact{position:absolute;top:468px;left:28px;right:28px;font-size:12px;line-height:1.45;color:var(--white)}
  .contact__title{text-align:center;font-size:17px;color:var(--sky-light);margin-bottom:6px}
  .contact__row{display:flex;gap:8px;align-items:flex-start;margin-bottom:3px}
  .contact__row svg{flex:0 0 12px;width:12px;height:12px;margin-top:3px;fill:var(--sky-light)}
  .contact__pair{display:grid;grid-template-columns:1fr 1.4fr;gap:3px 10px;margin-bottom:3px}
  .contact__form{margin-top:4px;color:var(--muted);font-size:11.5px}
  .brand{display:flex;align-items:center;gap:10px}
  .brand__mark{width:34px;height:34px;border-radius:50%;background:var(--sky)}
  .brand__name{font-family:"Oswald",Arial,sans-serif;font-weight:600;font-size:30px;color:var(--sky)}
  .faq-brand{position:absolute;top:728px;left:0;right:0;justify-content:center}
  .faq-foot{position:absolute;top:788px;left:28px;right:28px;display:flex;align-items:center;justify-content:center;gap:14px}
  .qr{width:58px;height:58px;background:var(--white);border:4px solid var(--white);outline:2px solid var(--sky-light)}
  .faq-web{font-size:14px;color:var(--white)}

  /* right panel */
  .panel--cover{background:var(--paper)}
  .cover-brand{position:absolute;top:48px;left:0;right:0;justify-content:center}
  .cover__photo{position:absolute;top:130px;left:0;right:0;height:300px;background:radial-gradient(ellipse at 55% 60%,#d9dde3 0%,#a9afb8 45%,#e9ebee 100%)}
  .cover__claim{position:absolute;top:470px;left:24px;right:24px;text-align:center;color:var(--white);font-weight:600;line-height:1.25}
  .cover__claim-lead{font-size:24px}
  .cover__claim-sub{font-size:21px;margin-top:10px}
  .cover__call{position:absolute;top:700px;left:20px;right:20px;text-align:center}
  .cover__call-head{font-size:26px;font-weight:600;color:var(--navy)}
  .cover__call .phones{font-size:24px;margin-top:2px}
  .cover__call .web{font-size:17px;margin-top:2px}
</style>
</head>
<body>
<main class="leaflet">

  <section class="panel panel--about">
    <svg class="deco" viewBox="0 0 373 867" preserveAspectRatio="none" aria-hidden="true">
      <polygon points="300,0 373,0 373,120" fill="var(--sky)"/>
      <polygon points="0,680 373,680 373,867 0,867" fill="var(--sky)"/>
      <polygon points="0,690 340,690 373,740 373,867 30,867 0,820" fill="var(--white)"/>
    </svg>
    <h2 class="about__title caps">Who we are</h2>
    <p class="about__text">Vehicle smart repair is a trade recognised alternative to the traditional body shop repair. The SMART (small to medium area repair technology) repair concept can be carried out at your home or place of work and at a price of more than 50% less than traditional body shop costs! One of the main benefits is that you do not have to lose the use of your vehicle for days while waiting for repairs. The Panelsmith can complete the repair within a day. This makes it a very convenient, cost effective alternative. Unlike traditional body shop repairs, only the area damaged needs to be refinished, thus preserving the integrity of the original paintwork. The Panelsmith uses a Varnel Waterbased paint system which is fully compliant with the 2004/42/CE European legislation, so enabling us to carry out repairs without the need for expensive spray booths or premises.</p>
    <div class="about__photo" role="img" aria-label="Photo of the company paint van and a repaired car parked outside a brick house"></div>
    <div class="about__cta">
      <p class="about__cta-head caps">Call today to arrange a free<br>no obligation estimate</p>
      <p class="phones"><svg viewBox="0 0 12 16"><rect x="1" y="0" width="10" height="16" rx="2"/></svg>07700900273<svg viewBox="0 0 12 16"><rect x="1" y="0" width="10" height="16" rx="2"/></svg>07700900418</p>
      <p class="web">www.quillardpanelworks.com</p>
    </div>
  </section>

  <section class="panel panel--faq">
    <svg class="deco" viewBox="0 0 373 867" preserveAspectRatio="none" aria-hidden="true">
      <polygon points="0,0 373,0 373,40 0,20" fill="var(--sky)"/>
      <polygon points="0,20 373,40 373,55 0,30" fill="var(--navy-2)"/>
    </svg>
    <div class="faq">
      <h2 class="faq__title">Frequently asked questions</h2>
      <div class="faq__item"><p class="faq__q">1. How long does a repair take?</p><p class="faq__a">The Panelsmith's repairs are usually carried out within a day, quite often within a few hours.</p></div>
      <div class="faq__item"><p class="faq__q">2. Are repairs guaranteed?</p><p class="faq__a">Yes. The Panelsmith's repairs are fully guaranteed.</p></div>
      <div class="faq__item"><p class="faq__q">3. Will there be any additional costs?</p><p class="faq__a">The cost given on the estimate is the total cost of the repair.</p></div>
      <div class="faq__item"><p class="faq__q">4. Have you got my car colour?</p><p class="faq__a">Yes, with the Varnel Waterbased paint system which complies with the 2004/42/CE European legislations we are able to mix in excess of 25,000 colours.</p></div>
      <div class="faq__item"><p class="faq__q">5. Where are the repairs carried out?</p><p class="faq__a">Usually at your home or place of work, with the only requirement being access to an electrical supply for a short time.</p></div>
    </div>
    <div class="contact">
      <h2 class="contact__title">Contact Information</h2>
      <p class="contact__row"><svg viewBox="0 0 12 12"><path d="M6 0 12 5H10V12H2V5H0Z"/></svg><span>Home 12 Hollin Row, Ashcombe, Wexshire AB1 2CD</span></p>
      <p class="contact__row"><svg viewBox="0 0 12 12"><path d="M2 0H5L6 3 4 5Q5 7 7 8L9 6 12 7V10Q12 12 10 12 0 12 0 2 0 0 2 0Z"/></svg><span>Office (answerphone) 01632 960581</span></p>
      <p class="contact__row"><svg viewBox="0 0 12 12"><rect x="0" y="2" width="12" height="8"/></svg><span>allstaff@quillardpanelworks.com</span></p>
      <div class="contact__pair">
        <p class="contact__row"><svg viewBox="0 0 12 12"><rect x="3" y="0" width="6" height="12" rx="1"/></svg><span>07700900273</span></p>
        <p>Derek Marlow<br>derek@quillardpanelworks.com</p>
        <p class="contact__row"><svg viewBox="0 0 12 12"><rect x="3" y="0" width="6" height="12" rx="1"/></svg><span>07700900418</span></p>
        <p>Keith Danton<br>keith@quillardpanelworks.com</p>
      </div>
      <p class="contact__form">Fill in the contact form on our website and upload a photo of the damage for a quick estimate.</p>
    </div>
    <div class="brand faq-brand"><span class="brand__mark"></span><span class="brand__name">The Panelsmith</span></div>
    <div class="faq-foot">
      <div class="qr" role="img" aria-label="QR code linking to the company website"></div>
      <p class="faq-web">www.quillardpanelworks.com</p>
    </div>
  </section>

  <section class="panel panel--cover">
    <svg class="deco" viewBox="0 0 373 867" preserveAspectRatio="none" aria-hidden="true">
      <polygon points="0,0 80,0 0,60" fill="var(--sky)"/>
      <polygon points="0,430 373,430 373,660 0,660" fill="var(--royal)"/>
      <polygon points="0,400 160,430 0,470" fill="var(--sky)"/>
      <polygon points="0,800 0,867 90,867" fill="var(--sky)"/>
      <polygon points="373,820 373,867 300,867" fill="var(--sky)"/>
    </svg>
    <div class="brand cover-brand"><span class="brand__mark"></span><span class="brand__name">The Panelsmith</span></div>
    <div class="cover__photo" role="img" aria-label="Photo of a silver SUV in a bright white studio"></div>
    <div class="cover__claim caps">
      <p class="cover__claim-lead">15 years experience in mobile body repairs.</p>
      <p class="cover__claim-sub">Quality mobile repires at a fraction of traditionals body shop costs</p>
    </div>
    <div class="cover__call">
      <p class="cover__call-head caps">Call us today :</p>
      <p class="phones">07700900273<svg viewBox="0 0 12 16"><rect x="1" y="0" width="10" height="16" rx="2"/></svg>07700900418</p>
      <p class="web">www.quillardpanelworks.com</p>
    </div>
  </section>

</main>
</body>
</html>
```